Non-profit sports organization needs templates for Word and InDesign

"Pelo Minis" is a non-profit organization in Winterthur, which supports the recruitment of young talent by the handball clubs in Winterthur. Every year we run several camps, a tournament for schoolchildren and several handball lessons at school.
During these activities there are always written information. So far we have not given much thought to the design. But since we think that a professional design will also lead to more interaction, we now turn to you as a designer.

For the communication with partners, sponsors, patrons, etc. we need a uniform appearance. Since different departments are currently working with different programs, we need a template for letters and documentation for Word and InDesign.

We will need the documentation template for project descriptions, information, etc.
The letter templates are needed to contact sponsors, authorities, patrons, etc.

Both the letter template and the documentation template should look modern. The design should be based on the existing flyers. Otherwise we have no other requirements so far.

Homepage: www.pelo-minis.ch

Target Market(s)

Letters, documentation or information to authorities, sponsors, associations, patrons, members, participants, etc.

Requirements
Must have
• In addition to the design, the templates should also contain a concept for titles, paragraphs, lists, etc. (colors / fonts / ...)

Word and Indesign templates

```html
<!DOCTYPE html>
<html lang="en">
<head>
<meta charset="utf-8">
<title>Pelo Minis – Documentation Template</title>
<link href="https://fonts.googleapis.com/css2?family=Lato:wght@400;700;900&display=swap" rel="stylesheet">
<style>
  :root {
    --bg: #e4e4e4;
    --paper: #f7f7f7;
    --ink: #222833;
    --body: #4a4a4a;
    --red: #e0121c;
    --red-dark: #c40d16;
    --orange: #f03a12;
    --blue: #1a8de0;
    --blue-light: #2aa6f0;
    --photo-hall: #b9a99a;
    --photo-dark: #5a4f4a;
    --photo-yellow: #c9b04a;
    --white: #ffffff;
  }
  * { box-sizing: border-box; margin: 0; padding: 0; }
  html, body { width: 1200px; height: 574px; overflow: hidden; }
  body { background: var(--bg); font-family: "Lato", Arial, sans-serif; color: var(--body); position: relative; }

  .page { position: absolute; top: 50px; width: 338px; height: 476px; background: var(--paper); overflow: hidden; }
  .page--cover { left: 58px; }
  .page--inner { left: 428px; }
  .page--back { left: 792px; }

  .abs { position: absolute; }
  .photo { position: absolute; }

  .body-text { font-size: 6.6px; line-height: 9.6px; text-align: justify; color: var(--body); }
  .body-text p + p { margin-top: 9px; }

  /* Cover */
  .cover-head { position: absolute; left: 0; top: 0; width: 338px; height: 165px; }
  .brand-name { font-weight: 900; font-size: 13px; letter-spacing: .2px; }
  .cover-brand { right: 12px; top: 22px; color: var(--red); }
  .cover-title { right: 8px; top: 77px; text-align: right; color: var(--white); }
  .cover-title h1 { font-size: 15.5px; font-weight: 700; }
  .cover-title p { font-size: 9.5px; line-height: 12px; margin-top: 4px; }
  .cover-date { right: 0; top: 137px; background: var(--orange); color: var(--white); font-weight: 700; font-size: 10.5px; padding: 3px 6px 3px 8px; }
  .cover-side { left: 0; top: 165px; width: 119px; height: 169px; background: var(--red-dark); color: var(--white); font-size: 7.6px; line-height: 10.8px; padding: 18px 10px 0 10px; }
  .cover-side-photo { left: 0; top: 334px; width: 119px; height: 142px; background: linear-gradient(180deg, #c42a2a 0%, #6e5a6a 55%, #d8cfc8 100%); }
  .cover-main { left: 133px; top: 199px; width: 192px; }
  .section-title { font-size: 11px; font-weight: 700; color: var(--ink); border-left: 2px solid var(--red); padding-left: 5px; margin-left: -7px; }
  .cover-main .body-text { margin-top: 3px; }
  .features-title { left: 134px; top: 290px; font-size: 9px; font-weight: 700; color: var(--orange); }
  .feature-list { left: 133px; top: 327px; width: 195px; list-style: none; }
  .feature-list li { position: relative; padding-left: 13px; font-size: 7.4px; line-height: 10px; color: var(--body); margin-bottom: 11px; }
  .feature-list li::before { content: ""; position: absolute; left: 1px; top: 2px; width: 7px; height: 6px; background: var(--red); border-radius: 1px; }

  /* Inner */
  .inner-photo { left: 0; top: 0; width: 118px; height: 476px; background: linear-gradient(180deg, #8c8580 0%, #b8a990 45%, #c9bfae 100%); }
  .paragraph-title { font-size: 10.5px; line-height: 13px; font-weight: 700; color: var(--ink); text-transform: uppercase; letter-spacing: .2px; }
  .inner-title { left: 139px; top: 30px; }
  .inner-copy { left: 141px; top: 60px; width: 185px; }
  .inner-photo-2 { left: 141px; top: 171px; width: 197px; height: 119px; background: linear-gradient(135deg, #a3968a 0%, #7c7fa8 50%, #c8beb3 100%); }
  .dot-list { list-style: none; }
  .dot-list li { position: relative; padding-left: 6px; font-size: 6.8px; line-height: 9.6px; color: var(--body); }
  .dot-list li::before { content: ""; position: absolute; left: 0; top: 3px; width: 3px; height: 3px; border-radius: 50%; background: var(--blue); }
  .inner-list { left: 141px; top: 300px; width: 190px; }
  .inner-list li { margin-bottom: 16.6px; }

  /* Back */
  .back-title { left: 25px; top: 37px; }
  .back-photo { left: 208px; top: 31px; width: 130px; height: 113px; background: linear-gradient(160deg, #b8a48c 0%, #e9e6e2 55%, #8b7d70 100%); }
  .back-list { left: 36px; top: 54px; width: 160px; }
  .back-list li { margin-bottom: 10px; text-align: justify; }
  .back-list li::before { background: var(--ink); }
  .back-list strong { color: var(--ink); }
  .back-copy { left: 25px; top: 176px; width: 293px; }
  .back-footer { left: 0; top: 321px; width: 338px; height: 155px; }
  .back-brand { right: 24px; top: 400px; color: var(--white); font-size: 15px; }
  .back-contact { right: 22px; top: 432px; color: var(--white); font-weight: 700; font-size: 9.2px; line-height: 14px; text-align: left; }
</style>
</head>
<body>

<!-- Cover page -->
<section class="page page--cover">
  <svg class="cover-head" viewBox="0 0 338 165" aria-hidden="true">
    <polygon points="0,0 258,0 158,165 0,165" fill="var(--photo-hall)"/>
    <polygon points="208,48 338,48 338,165 138,165" fill="var(--blue)"/>
    <polygon points="208,48 338,48 338,70 194,70" fill="var(--blue-light)"/>
  </svg>
  <div class="photo" role="img" aria-label="Photo of a young handball player jumping to throw while a defender blocks" style="left:0;top:0;width:170px;height:165px;clip-path:polygon(0 0,100% 0,88% 34%,64% 100%,0 100%);background:linear-gradient(160deg,#c9c2bb 0%,#7a6e68 50%,#b23a36 100%);"></div>
  <div class="abs brand-name cover-brand">Pelo Minis</div>
  <div class="abs cover-title">
    <h1>Main header Title here</h1>
    <p>Event Description Text here Event<br>Description Text here</p>
  </div>
  <div class="abs cover-date">EVENT DATE HERE</div>

  <div class="abs cover-side">Lorem Ipsum is simply dummy text of the printing and typesetting industry. Lorem Ipsum has been the industry's standard dummy text ever since the 1500s, when an unknown printer took a galley of type and scrambled it to make a type specimen book. It has survived not only five centuries, but also the leap into electronic typesetting, remaining essentially</div>
  <div class="photo cover-side-photo" role="img" aria-label="Photo of girls looking at a phone in a sports hall"></div>

  <div class="abs cover-main">
    <h2 class="section-title">What is Lorem Ipsum?</h2>
    <p class="body-text">Lorem Ipsum is simply dummy text of the printing and typesetting industry. Lorem Ipsum has been the industry's standard dummy text ever since the 1500s, when an unknown printer took a galley of type and scrambled it to make a type specimen book. It has survived not only five centuries, but also the leap into electronic typesetting,</p>
  </div>
  <h3 class="abs features-title">Our Features</h3>
  <ul class="abs feature-list">
    <li>Survived not only five centuries, but also the leap into electronic typesetting,</li>
    <li>Survived not only five centuries, but also the leap into electronic typesetting,</li>
    <li>Survived not only five centuries, but also the leap into electronic typesetting,</li>
    <li>Survived not only five centuries, but also the leap into electronic typesetting,</li>
  </ul>
</section>

<!-- Inner page -->
<section class="page page--inner">
  <div class="photo inner-photo" role="img" aria-label="Photo of a female handball player in a yellow shirt running with the ball"></div>
  <h2 class="abs paragraph-title inner-title">Paragraph header title here<br>in two lins</h2>
  <div class="abs body-text inner-copy">
    <p>Lorem Ipsum is simply dummy text of the printing and typesetting industry. Lorem Ipsum has been the industry's standard dummy text ever since the 1500s, when an unknown printer took a galley of type and scrambled it to make a type specimen book. It has survived not only five centuries, but also the leap into electronic typesetting,</p>
    <p>Lorem Ipsum is simply dummy text of the printing and typesetting industry. Lorem Ipsum has been the industry's standard dummy text ever since the 1500s, when an unknown printer took a galley of type and scr</p>
  </div>
  <div class="photo inner-photo-2" role="img" aria-label="Photo of children sitting on a gym floor raising their hands"></div>
  <ul class="abs dot-list inner-list">
    <li>Lorem Ipsum is simply dummy text of the printing and typesetting industry. Lorem Ipsum</li>
    <li>Lorem Ipsum is simply dummy text of the printing and typesetting industry. Lorem Ipsum</li>
    <li>Lorem Ipsum is simply dummy text of the printing and typesetting industry. Lorem Ipsum</li>
    <li>Lorem Ipsum is simply dummy text of the printing and typesetting industry. Lorem Ipsum</li>
    <li>Lorem Ipsum is simply dummy text of the printing and typesetting industry. Lorem Ipsum</li>
  </ul>
</section>

<!-- Back page -->
<section class="page page--back">
  <h2 class="abs paragraph-title back-title">Paragraph header title</h2>
  <ul class="abs dot-list back-list">
    <li><strong>Lorem Ipsum is simply</strong> dummy text of the printing and typesetting industry. Lorem Ipsum has been the industry's standard dummy text ever since the 1500s, when an unknown printer</li>
    <li><strong>Lorem Ipsum is simply</strong> dummy text of the printing and typesetting industry. Lorem Ipsum has been the industry's standard dummy text ever since the 1500s, when an unknown printer</li>
  </ul>
  <div class="photo back-photo" role="img" aria-label="Photo of young players at a handball camp, one raising an arm"></div>
  <div class="abs body-text back-copy">
    <p>Lorem Ipsum is simply dummy text of the printing and typesetting industry. Lorem Ipsum has been the industry's standard dummy text ever since the 1500s, when an unknown printer took a galley of type and scrambled it to make</p>
    <p>A type specimen book. It has survived not only five centuries, but also the leap into electronic typesetting, Lorem Ipsum is simply dummy text of the printing and typesetting industry. Lorem Ipsum has been the industry's standard dummy text ever since the 1500s, when an unknown printer took a galley of type and scrambled it to make a type specimen book. It has survived not only five centuries, but also the leap into electronic typesetting,</p>
    <p>Lorem Ipsum is simply dummy text of the printing and typesetting industry. Lorem Ipsum has been the industry's standard dummy text ever since the</p>
  </div>
  <svg class="abs back-footer" viewBox="0 0 338 155" aria-hidden="true">
    <rect x="0" y="40" width="338" height="4" fill="var(--blue)"/>
    <rect x="0" y="44" width="338" height="111" fill="var(--red)"/>
  </svg>
  <div class="photo" role="img" aria-label="Photo of two boys playing handball in a sports hall" style="left:0;top:321px;width:238px;height:155px;clip-path:polygon(24% 0,100% 0,67% 100%,0 100%,0 72%);background:linear-gradient(150deg,#c8bdb0 0%,#8d7f74 50%,#d6cfc6 100%);"></div>
  <div class="abs brand-name back-brand">Pelo Minis</div>
  <div class="abs back-contact">www.pelo-minis.ch<br>info@pelo-minis.ch</div>
</section>

</body>
</html>
```